label design for our sauces - please note not a flyer - but a LABEL for a jam & sauce jar
I have attached a sample of a few done by a friend. They are ok but I want something more please.
I am looking for it to be a bit sharper, font like the logo and some separation of the areas on the sides of the labels. Lines or dots or something.
I do also want to consider adding a piece of fruit as either a nice image or a stock line drawing. Id like a few options please? we have in total 12 labels we need asap and then we will want about another 12 after that.
See our competitors that we are trying to take inspiration from.
https://www.fallowmere.com.au - see particularly their strawberry jam label
also see https://www.tilvanes.com.au as a smaple of a nice whaite label but We want the trees to be a color as well as the top and bottom band.
Also we want 2 ranges, one with the white label and color on the band and the tree but the rest black text and then a black label with white text and a gold bad and leaves on the tree.
Can you please take these guides and create something please. the size of the labels to print is 60x160
Id like to get something in the next 24 hours if possible as I really need to get this completed this week.....

```html
<!DOCTYPE html>
<html lang="en">
<head>
<meta charset="utf-8">
<title>Marrow's Pantry – Pineapple Rum Jam Labels</title>
<link rel="stylesheet" href="https://fonts.googleapis.com/css2?family=Barlow:wght@300;400;700&family=Barlow+Condensed:wght@600&family=Lora:wght@400&display=swap">
<style>
  :root {
    --stage: #e5b400;
    --band: #efe33c;
    --accent: #efe33c;
    --white-label: #ffffff;
    --black-label: #0c0c0c;
    --ink-dark: #141414;
    --ink-light: #f2f2f2;
    --fruit-tone: linear-gradient(160deg, #d9d9d9 0%, #8a8a8a 55%, #efe33c 56%, #e4d630 100%);
  }
  * { box-sizing: border-box; margin: 0; padding: 0; }
  html, body { width: 1200px; height: 900px; overflow: hidden; }
  body {
    background: var(--stage);
    display: flex;
    align-items: center;
    justify-content: center;
    gap: 90px;
    font-family: "Barlow", sans-serif;
  }

  .label {
    width: 400px;
    height: 340px;
    display: flex;
    flex-direction: column;
    box-shadow: 0 18px 30px rgba(120, 80, 0, 0.25);
  }
  .label__band { height: 12px; background: var(--band); }
  .label__panel {
    flex: 1;
    display: flex;
    flex-direction: column;
    align-items: center;
    justify-content: center;
    padding: 0 60px;
  }
  .label--white .label__panel { background: var(--white-label); color: var(--ink-dark); --rule: var(--ink-dark); }
  .label--black .label__panel { background: var(--black-label); color: var(--ink-light); --rule: var(--ink-light); }

  .brand { display: flex; align-items: center; gap: 8px; }
  .brand__mark { width: 14px; height: 14px; background: var(--accent); }
  .brand__name {
    font-family: "Barlow Condensed", sans-serif;
    font-weight: 600;
    font-size: 36px;
    line-height: 1;
    letter-spacing: 0.5px;
  }
  .brand__tagline {
    font-family: "Lora", serif;
    font-size: 10.5px;
    letter-spacing: 1.4px;
    text-transform: uppercase;
    margin-top: 6px;
  }

  .dotted-rule {
    width: 250px;
    border-top: 2px dotted var(--rule);
    margin: 14px 0;
  }

  .product { display: flex; align-items: stretch; width: 250px; }
  .product__names { flex: 1; }
  .product__flavour {
    font-weight: 300;
    font-size: 19px;
    text-transform: uppercase;
    padding-bottom: 4px;
    border-bottom: 1px solid var(--rule);
  }
  .product__type {
    font-weight: 700;
    font-size: 66px;
    line-height: 1;
    letter-spacing: 3px;
    margin-top: 4px;
  }
  .divider { width: 1px; background: var(--rule); margin: 0 8px; }
  .product__fruit {
    width: 54px;
    height: 90px;
    background: var(--fruit-tone);
    border-radius: 4px;
  }

  .claims { display: flex; align-items: flex-start; width: 250px; }
  .claims__text { flex: 1; }
  .claims__natural {
    font-weight: 300;
    font-size: 14px;
    text-transform: uppercase;
    letter-spacing: -0.3px;
    padding-bottom: 3px;
    border-bottom: 1px solid var(--rule);
  }
  .claims__gluten {
    font-weight: 700;
    font-size: 18px;
    letter-spacing: 4px;
    text-transform: uppercase;
    margin-top: 3px;
  }
  .claims .divider { align-self: stretch; }
  .claims__weight { font-weight: 300; font-size: 15px; padding-top: 8px; }
</style>
</head>
<body>

  <article class="label label--white">
    <div class="label__band"></div>
    <div class="label__panel">
      <div class="brand">
        <span class="brand__mark"></span>
        <span class="brand__name">MARROW'S PANTRY</span>
      </div>
      <p class="brand__tagline">Proudly Australian since 1987</p>
      <div class="dotted-rule"></div>
      <div class="product">
        <div class="product__names">
          <p class="product__flavour">Pineapple Rum</p>
          <p class="product__type">JAM</p>
        </div>
        <span class="divider"></span>
        <div class="product__fruit" role="img" aria-label="Line drawing of a pineapple with a yellow accent shape"></div>
      </div>
      <div class="dotted-rule"></div>
      <div class="claims">
        <div class="claims__text">
          <p class="claims__natural">All natural ingredients</p>
          <p class="claims__gluten">Gluten free</p>
        </div>
        <span class="divider"></span>
        <p class="claims__weight">215g</p>
      </div>
    </div>
    <div class="label__band"></div>
  </article>

  <article class="label label--black">
    <div class="label__band"></div>
    <div class="label__panel">
      <div class="brand">
        <span class="brand__mark"></span>
        <span class="brand__name">MARROW'S PANTRY</span>
      </div>
      <p class="brand__tagline">Proudly Australian since 1987</p>
      <div class="dotted-rule"></div>
      <div class="product">
        <div class="product__names">
          <p class="product__flavour">Pineapple Rum</p>
          <p class="product__type">JAM</p>
        </div>
        <span class="divider"></span>
        <div class="product__fruit" role="img" aria-label="Line drawing of a pineapple with a yellow accent shape"></div>
      </div>
      <div class="dotted-rule"></div>
      <div class="claims">
        <div class="claims__text">
          <p class="claims__natural">All natural ingredients</p>
          <p class="claims__gluten">Gluten free</p>
        </div>
        <span class="divider"></span>
        <p class="claims__weight">215g</p>
      </div>
    </div>
    <div class="label__band"></div>
  </article>

</body>
</html>
```